App for Lawyers & Accountants needs 'Professional' Styling

We want to style our app to convey a 'Professional' appearance. It's used by Lawyers, Accountants, Doctors etc. who take their work very seriously.

We currently trying to follow keystrel layout guidelines, but we find our app looks very bland. I've uploaded a screenshot of our current app, and two mock-ups of more stylized versions, but we're not happy with those mock-ups.

We'd like to see alternate designs for those two mock-ups, that look much more professional.

The specific elements we'd like to improve/focus on are:
* Colour of the top and left nav bars
* Appearance of the left nav, size, icons spacing
* Appearance of the buttons on the top right, so the user knows they are buttons they can press
* Spacing of the dashboard, background colour and spacing, colour/layout of the 'overdue' and 'todo' accordion headings in the 'my tasks' section.
* List view background grey, to be consistent with dashboard, but unobtrusive
* List view tabs to be obvious as tabs, but 'saved searches', filters and the export icon to still be associated with the data displayed, but it should be obvious to the user that those are different buttons, not just more tabs. (I.e. the filters button opens a panel below it that allows the user to filter the data in the list.)
* General appearance of the popup menu when you push the 'add' button on the top right

However, despite those specifics I'm sure it's all the subtle elements of the design that make a big difference.

Our brand colour is 1D4F91, and we use A20067 as a secondary colour in print media, (although it doesn't seem to work to well within the app.) Our brand font is signika. We'd like the designs to be based on those colours & font.

Target Market(s)

Professional people, Lawyers, Accountants, Doctors etc.

Font styles to use
Sans Serif
Other font styles liked:
• Signika

Colors
0255a3

Requirements
Must have
• The most 'Professional' experience/quality possible. Think the quality & brand image of vantrel desk, but taken to a higher level.
• An example/mock-up of the dashboard, list view and 'add' item popup menu
• Display the dashboard cards with the same information as our mock-ups - the information there is important and we don't have any extra cards to add (in the near term)
Nice to have
• Various colour combinations for the top and left nav bars, based on our primary blue brand colour, and perhaps some shade of dark grey.

```html
<!DOCTYPE html>
<html lang="en">
<head>
<meta charset="utf-8">
<title>Matters – My Matters</title>
<link rel="stylesheet" href="https://fonts.googleapis.com/css2?family=Signika:wght@300;400;600&display=swap">
<style>
  :root {
    --brand: #1d4f91;
    --brand-dark: #143a70;
    --link: #1d5aa3;
    --accent: #a20067;
    --ink: #2d3238;
    --muted: #8a9097;
    --line: #dfe3e8;
    --page: #f3f4f6;
    --white: #ffffff;
  }
  * { box-sizing: border-box; margin: 0; padding: 0; }
  html, body { width: 1200px; height: 729px; overflow: hidden; }
  body { font-family: "Signika", sans-serif; background: var(--page); color: var(--ink); position: relative; }

  .sidebar { position: absolute; left: 0; top: 0; width: 76px; height: 729px;
    background: linear-gradient(180deg, #1f569c 0%, var(--brand) 55%, #17457f 100%); }
  .sidebar .brand { height: 67px; display: flex; align-items: center; justify-content: center; background: #1a4a88; }
  .brand-mark { width: 40px; height: 40px; border-radius: 50%; background: #3a5f8f; color: #fff;
    font-size: 9px; display: flex; align-items: center; justify-content: center; }
  .nav-item { height: 63px; display: flex; align-items: center; justify-content: center; border-bottom: 1px solid rgba(255,255,255,.12); }
  .nav-item svg { width: 20px; height: 20px; stroke: #a9c2e3; fill: none; stroke-width: 1.4; }
  .nav-item.active svg { stroke: #fff; }
  .nav-bottom { position: absolute; left: 0; bottom: 0; width: 76px; border-top: 1px solid rgba(255,255,255,.12); }
  .nav-bottom .nav-item:last-child { border-bottom: 0; }

  .topbar { position: absolute; left: 76px; top: 0; right: 0; height: 67px; background: var(--white); border-bottom: 1px solid var(--line); }
  .page-title { position: absolute; left: 20px; top: 24px; font-size: 16px; font-weight: 400; }
  .search { position: absolute; left: 491px; top: 17px; width: 254px; height: 35px; border: 1px solid #c8ced6;
    display: flex; align-items: center; padding-left: 10px; gap: 8px; font-size: 11px; color: var(--muted); }
  .search svg { width: 15px; height: 15px; stroke: var(--link); fill: none; stroke-width: 1.5; }
  .icon-btn { position: absolute; top: 17px; width: 36px; height: 35px; border: 1px solid var(--link);
    display: flex; align-items: center; justify-content: center; }
  .icon-btn svg { width: 17px; height: 17px; stroke: var(--link); fill: none; stroke-width: 1.5; }
  .avatar { position: absolute; left: 886px; top: 0; width: 67px; height: 67px;
    background: linear-gradient(160deg, #a57f66, #d8c2b0 60%, #7e9fbd); }
  .user { position: absolute; left: 953px; top: 0; width: 111px; height: 67px; background: var(--brand); color: #fff; padding: 18px 0 0 15px; }
  .user small { display: block; font-size: 10px; color: #cfe0f4; }
  .user strong { display: block; font-size: 13px; font-weight: 600; }
  .user svg { position: absolute; right: 9px; top: 29px; width: 11px; height: 8px; stroke: #fff; fill: none; stroke-width: 1.4; }

  .toolbar { position: absolute; left: 97px; top: 96px; width: 1065px; height: 18px; font-size: 13px; }
  .crumbs { display: flex; align-items: center; gap: 7px; }
  .crumbs a { color: var(--link); text-decoration: none; }
  .crumbs svg { width: 6px; height: 10px; stroke: var(--ink); fill: none; stroke-width: 1.3; }
  .actions { position: absolute; top: 0; right: 0; display: flex; gap: 0; }
  .action { position: absolute; display: flex; align-items: center; gap: 5px; color: var(--link); white-space: nowrap; top: 0; }
  .action svg.ic { width: 14px; height: 14px; stroke: var(--accent); fill: none; stroke-width: 1.4; }
  .action svg.chev { width: 8px; height: 6px; stroke: var(--link); fill: none; stroke-width: 1.3; }

  .card { position: absolute; left: 96px; top: 137px; width: 1066px; height: 498px; background: var(--white); border: 1px solid var(--line); }
  .tabs { height: 55px; border-bottom: 1px solid var(--line); position: relative; }
  .tab { position: absolute; top: 24px; font-size: 10px; letter-spacing: 1.3px; color: #4b5158; }
  .tab.active { font-weight: 600; color: var(--ink); }
  .tab.active::after { content: ""; position: absolute; left: 0; right: -2px; top: 22px; height: 2px; background: var(--brand); }

  table { position: absolute; left: 22px; top: 90px; width: 1043px; border-collapse: collapse; font-size: 12.5px; }
  th { text-align: left; font-size: 10px; letter-spacing: 1.2px; font-weight: 600; height: 20px; vertical-align: top; }
  td { height: 60px; border-bottom: 1px solid var(--line); }
  tbody tr:first-child td { height: 60px; }
  td a { color: var(--link); text-decoration: none; }
  .c-title { width: 459px; } .c-client { width: 145px; } .c-area { width: 171px; } .c-status { width: 134px; }

  .pager { position: absolute; left: 812px; top: 447px; display: flex; align-items: center; font-size: 11px; }
  .per { color: var(--link); display: flex; align-items: center; gap: 3px; }
  .per svg { width: 7px; height: 5px; stroke: var(--link); fill: none; stroke-width: 1.2; }
  .per-label { margin-left: 6px; margin-right: 27px; }
  .page { width: 22px; height: 22px; border: 1px solid #c8ced6; display: flex; align-items: center; justify-content: center; color: var(--muted); margin-right: 4px; font-size: 10px; }
  .page.current { border-color: var(--link); color: var(--link); }

  .footer { position: absolute; right: 38px; top: 692px; font-size: 9px; color: #4b5158; }
</style>
</head>
<body>
  <nav class="sidebar">
    <div class="brand"><div class="brand-mark">LOGO</div></div>
    <div class="nav-item"><svg viewBox="0 0 20 20"><rect x="2" y="10" width="4" height="7"/><rect x="8" y="6" width="4" height="11"/><rect x="14" y="3" width="4" height="14"/></svg></div>
    <div class="nav-item active"><svg viewBox="0 0 20 20"><path d="M9 3l6 6-3 3-6-6z"/><path d="M9 9l-6 6 2 2 6-6"/><path d="M11 17h7"/></svg></div>
    <div class="nav-item"><svg viewBox="0 0 20 20"><circle cx="10" cy="7" r="4"/><path d="M3 18c1-4 4-6 7-6s6 2 7 6"/></svg></div>
    <div class="nav-item"><svg viewBox="0 0 20 20"><path d="M5 14V9a5 5 0 0110 0v5l1.5 2h-13z"/><path d="M8.5 17.5a1.5 1.5 0 003 0"/></svg></div>
    <div class="nav-item"><svg viewBox="0 0 20 20"><path d="M15 9l-6 6a3 3 0 01-4-4l7-7a2 2 0 013 3l-7 7a1 1 0 01-1.5-1.5l6-6"/></svg></div>
    <div class="nav-item"><svg viewBox="0 0 20 20"><path d="M3 10a7 7 0 107-7 7 7 0 00-6 3.5"/><path d="M3 3v4h4"/><path d="M10 6v4l3 2"/></svg></div>
    <div class="nav-bottom">
      <div class="nav-item"><svg viewBox="0 0 20 20"><circle cx="10" cy="10" r="3"/><path d="M10 2v2.5M10 15.5V18M2 10h2.5M15.5 10H18M4.3 4.3l1.8 1.8M13.9 13.9l1.8 1.8M4.3 15.7l1.8-1.8M13.9 6.1l1.8-1.8"/></svg></div>
      <div class="nav-item"><svg viewBox="0 0 20 20"><path d="M17 10H3M9 4l-6 6 6 6"/></svg></div>
    </div>
  </nav>

  <header class="topbar">
    <h1 class="page-title">Matters</h1>
    <div class="search"><svg viewBox="0 0 16 16"><circle cx="9" cy="7" r="5"/><path d="M5.5 10.5L2 14"/></svg>Search</div>
    <div class="icon-btn" style="left:752px"><svg viewBox="0 0 18 18"><path d="M9 2v14M2 9h14"/></svg></div>
    <div class="icon-btn" style="left:793px"><svg viewBox="0 0 18 18"><path d="M2 9a7 7 0 107-7 7 7 0 00-6 3.5"/><path d="M2.5 2.5v3.5H6"/><path d="M9 5.5V9l2.5 2"/></svg></div>
    <div class="icon-btn" style="left:835px"><svg viewBox="0 0 18 18"><path d="M4.5 13V8.5a4.5 4.5 0 019 0V13l1.3 1.5H3.2z"/><path d="M7.5 16a1.5 1.5 0 003 0"/></svg></div>
    <div class="avatar" role="img" aria-label="Profile photo of the signed-in user"></div>
    <div class="user"><small>Welcome</small><strong>Jane Smith</strong><svg viewBox="0 0 11 8"><path d="M1 2l4.5 4L10 2"/></svg></div>
  </header>

  <div class="toolbar">
    <div class="crumbs"><a href="#">Matters</a><svg viewBox="0 0 6 10"><path d="M1 1l4 4-4 4"/></svg><span>My Matters</span></div>
    <div class="action" style="left:756px"><svg class="ic" viewBox="0 0 14 14"><path d="M9 1H2v12h5"/><path d="M9 1l3 3v3"/><circle cx="10" cy="10.5" r="2.2"/></svg>Saved Searches<svg class="chev" viewBox="0 0 8 6"><path d="M1 1.5l3 3 3-3"/></svg></div>
    <div class="action" style="left:910px"><svg class="ic" viewBox="0 0 14 14"><path d="M1 3h12M1 7h12M1 11h12"/><circle cx="4" cy="3" r="1.3"/><circle cx="10" cy="7" r="1.3"/><circle cx="6" cy="11" r="1.3"/></svg>Filters<svg class="chev" viewBox="0 0 8 6"><path d="M1 1.5l3 3 3-3"/></svg></div>
    <div class="action" style="left:1014px"><svg class="ic" viewBox="0 0 14 14"><path d="M9 4V1H2v12h7v-3"/><path d="M6 7h7M10.5 4.5L13 7l-2.5 2.5"/></svg>Export</div>
  </div>

  <main class="card">
    <div class="tabs">
      <span class="tab active" style="left:19px">MY MATTERS</span>
      <span class="tab" style="left:143px">RECENT MATTERS</span>
      <span class="tab" style="left:293px">ALL MATTERS</span>
    </div>
    <table>
      <thead>
        <tr><th class="c-title">TITLE</th><th class="c-client">CLIENT</th><th class="c-area">PRACTICE AREA</th><th class="c-status">STATUS</th><th>LAST UPDATED</th></tr>
      </thead>
      <tbody>
        <tr><td><a href="#">Abbott v. Moore concerning sale #707</a></td><td><a href="#">M Hamill</a></td><td>Conveyancing</td><td>Sign up</td><td>30/06/2017</td></tr>
        <tr><td><a href="#">Abernathy v. Director of Public Prosecutions con deceased #310</a></td><td><a href="#">Nicholas Inc.</a></td><td>Estates</td><td>Settlement</td><td>16/04/2017</td></tr>
        <tr><td><a href="#">Abernathy v. Director of Public Prosecutions con investment #578</a></td><td><a href="#">Little &amp; Rogan</a></td><td>Property</td><td>Settlement</td><td>05/03/2017</td></tr>
        <tr><td><a href="#">Abernathy v. Director of Public Prosecutions con work cover #295</a></td><td><a href="#">D’Amore Zieman</a></td><td>Personal Injury</td><td>Sign up</td><td>02/09/2017</td></tr>
        <tr><td><a href="#">Abernathy v. Schmitt concerning retail lease #668</a></td><td><a href="#">Witting &amp; Leucscke</a></td><td>Property</td><td>Settlement</td><td>15/11/2017</td></tr>
      </tbody>
    </table>
    <div class="pager">
      <span class="per">20<svg viewBox="0 0 7 5"><path d="M1 1l2.5 2.5L6 1"/></svg></span>
      <span class="per-label">per page</span>
      <span class="page current">1</span><span class="page">2</span><span class="page">3</span><span class="page">4</span><span class="page">5</span>
    </div>
  </main>

  <footer class="footer">CALDERWYN © 2018</footer>
</body>
</html>
```